I need a website built for my organization.
We are the world's largest network of music producers.
The website should be professional, sharp, and high quality., We need a website built for The Halvern Sound Guild. We are one of the World's largest association of music producers.
The site must be professional, sharp, and high quality., I need a website built for my organization.
The site must be professional, sharp, and high quality.
Somewhere in the top half of the site there should be a form for the user to fill out. The details of the form are as follows:
Title (large and bold): Contact Us or Submit Your Music
Fields to include (* = required): First Name*, Last Name*, Age, Zip Code, Email Address*, Daytime Phone, Evening Phone, Comments
Then, there will be a "submit" button to proceed to next step of form. Just below the "submit" button, should be the following verbiage: "After submitting, you will have the opportunity to upload demos of your music (optional) and provide other pertinent information about yourself, band, or group."
Target Market(s)
Music producers and aspiring musicians
Industry/Entity Type
Group
Colors
Designer to choose colors to be used in the design.
Look and feel

```html
<!DOCTYPE html>
<html lang="en">
<head>
<meta charset="utf-8">
<title>The Halvern Sound Guild</title>
<link href="https://fonts.googleapis.com/css2?family=Montserrat:wght@500;700;800&family=Raleway:wght@500;600;700&family=Cinzel:wght@600&family=Oswald:wght@500&display=swap" rel="stylesheet">
<style>
:root{
  --bg:#0d0d0d;
  --pink:#ff4466;
  --orange:#ff5b3a;
  --red:#d3142c;
  --panel:#e9e9ea;
  --text-light:#e6e6e6;
  --muted:#9a9a9a;
  --white:#ffffff;
}
*{box-sizing:border-box;margin:0;padding:0}
html,body{width:1010px;height:1200px;overflow:hidden}
body{position:relative;background:radial-gradient(ellipse at 50% 35%,#2a2a2a 0%,#111 55%,#070707 100%);font-family:Arial,Helvetica,sans-serif;color:var(--text-light)}
.abs{position:absolute}
/* header */
.brand{left:94px;top:25px;display:flex;align-items:center;gap:9px}
.brand-mark{width:39px;height:39px;border-radius:8px;background:linear-gradient(var(--pink),var(--orange))}
.brand-name{font-family:Montserrat,sans-serif;font-weight:800;font-size:21px;line-height:22px;color:var(--white)}
.brand-sub{font-family:Montserrat,sans-serif;font-weight:500;font-size:12.5px;color:var(--white)}
.social{left:756px;top:36px;display:flex;gap:9px}
.social span{width:22px;height:22px;border-radius:50%;background:var(--white)}
/* nav */
.nav{left:94px;top:91px;width:819px;height:37px;border-radius:8px 8px 0 0;background:linear-gradient(90deg,var(--pink),#ff4d55 60%,var(--orange));display:flex;align-items:center;padding:0 6px}
.nav a{font-family:Montserrat,sans-serif;font-weight:700;font-size:10px;color:var(--white);text-decoration:none;letter-spacing:.2px;flex:1 1 auto;text-align:center;border-right:1px solid rgba(255,255,255,.45);line-height:19px;white-space:nowrap}
.nav a:last-child{border-right:0}
/* slider */
.hero{left:94px;top:138px;width:819px;height:294px;border:3px solid var(--white);background:#111}
.hero-photo{position:absolute;inset:5px;background:linear-gradient(180deg,#4a3a50 0%,#6a5a6e 30%,#2c2230 60%,#0c0a0d 100%)}
.hero-title{left:373px;top:188px;width:414px;height:50px;background:linear-gradient(90deg,rgba(200,20,60,.92),rgba(200,20,60,.55));font-family:Cinzel,serif;font-weight:600;font-size:14.5px;letter-spacing:.5px;color:var(--white);display:flex;align-items:center;padding-left:7px}
/* panel */
.panel{left:0;top:0}
.sec-title{font-family:Raleway,sans-serif;font-weight:600;font-size:14px;letter-spacing:1.6px;color:var(--red)}
.thumb{top:483px;width:116px;height:79px}
.circ-btn{width:24px;height:24px;border-radius:50%;background:#a6a6a6;display:flex;align-items:center;justify-content:center}
.awards{left:645px;top:480px;width:242px;list-style:none}
.awards li{font-size:10.5px;color:#333;height:27px;line-height:20px;border-bottom:1px solid #c9c9c9;padding-left:12px;position:relative;white-space:nowrap}
.awards li:last-child{border-bottom:0}
.awards li::before{content:"»";position:absolute;left:0;font-size:9px;color:#444}
.more{left:826px;top:618px;font-size:9.5px;font-style:italic;color:var(--red)}
.dot{width:15px;height:15px;border-radius:50%;background:#ddd;top:619px}
/* blog */
.blog-title{left:98px;top:658px;font-family:Raleway,sans-serif;font-weight:500;font-size:22px;color:var(--white)}
.blog-title b{color:var(--red);font-weight:600}
.rule{left:100px;top:688px;width:505px;height:1px;background:#444}
.post-img{width:180px;height:123px;border:1px solid var(--white)}
.post-text{left:293px;width:330px;font-size:10.5px;line-height:16.8px;color:var(--text-light)}
.meta{left:293px;font-size:11px;color:var(--muted);display:flex;gap:18px;align-items:center}
.meta i{display:inline-block;width:11px;height:11px;background:var(--muted);margin-right:6px;vertical-align:-1px;border-radius:2px}
/* form */
.form{left:654px;top:666px;width:257px;height:366px;border:1px solid #3a3a3a;border-radius:3px;background:repeating-linear-gradient(45deg,#141414 0 3px,#1b1b1b 3px 6px)}
.form-title{position:absolute;left:0;top:9px;width:100%;text-align:center;font-family:Raleway,sans-serif;font-weight:700;font-size:17px;color:var(--white);letter-spacing:.5px}
.row{position:absolute;left:0;width:100%}
.row label{position:absolute;right:176px;top:3px;font-size:10.5px;color:var(--white);white-space:nowrap}
.row label em{font-style:normal;color:var(--pink)}
.row span{position:absolute;left:88px;width:149px;height:19px;background:var(--white)}
.submit{position:absolute;left:151px;top:274px;width:86px;height:21px;border-radius:2px;background:linear-gradient(#ff6a3a,#f0391c);font-family:Oswald,sans-serif;font-weight:500;font-size:13px;letter-spacing:.5px;color:var(--white);display:flex;align-items:center;justify-content:center}
.form-note{position:absolute;left:12px;top:302px;width:231px;font-size:8.5px;line-height:11px;color:#bdbdbd}
/* partners + footer */
.footer-band{left:0;top:1096px;width:1010px;height:104px;background:linear-gradient(90deg,#ff3d66,#ff4a52 50%,#ff5c3a)}
.partners{left:98px;top:1048px;width:814px;height:83px;border-radius:9px;background:linear-gradient(#f2f2f2,#cfcfcf)}
.badge{position:absolute;top:30px;width:100px;height:22px;border-radius:4px;background:#8a8a8a}
.foot-brand{left:93px;top:1146px;display:flex;align-items:center;gap:7px}
.foot-brand .brand-mark{width:32px;height:32px;background:rgba(255,255,255,.35)}
.foot-brand .brand-name{font-size:17px;line-height:18px;color:rgba(255,255,255,.75)}
.foot-brand .brand-sub{font-size:10px;color:rgba(255,255,255,.75)}
.foot-links{left:272px;top:1152px;font-size:10.5px;color:var(--white)}
.foot-links a{color:var(--white);text-decoration:none}
.foot-links .sep{margin:0 10px}
.copy{left:272px;top:1172px;font-size:10.5px;color:var(--white)}
.foot-social{left:764px;top:1151px;display:flex;gap:9px}
.foot-social span{width:30px;height:30px;border-radius:50%;background:rgba(255,255,255,.35)}
</style>
</head>
<body>

<header>
  <div class="abs brand">
    <div class="brand-mark"></div>
    <div><div class="brand-name">Halvern</div><div class="brand-sub">The Halvern Sound Guild</div></div>
  </div>
  <div class="abs social" aria-label="Social links"><span></span><span></span><span></span><span></span><span></span></div>
  <nav class="abs nav">
    <a>HOME</a><a>PHOTOS</a><a>VIDEOS</a><a>ARTISTS</a><a>EVENTS</a><a>DISCOGRAPHY</a><a>SHOP</a><a>BLOG</a><a>CONTACT</a>
  </nav>
</header>

<section class="abs hero">
  <div class="hero-photo" role="img" aria-label="Concert crowd with hands raised under stage lights"></div>
</section>
<div class="abs hero-title">WELCOME TO THE HALVERN SOUND GUILD</div>

<svg class="abs panel" width="1010" height="700" aria-hidden="true">
  <path d="M94,431 H913 V624 Q913,634 903,634 H662 Q645,634 637,618 Q627,598 603,598 H104 Q94,598 94,588 Z" fill="#e9e9ea"/>
</svg>

<h2 class="abs sec-title" style="left:103px;top:449px">PHOTO GALLERY</h2>
<div class="abs circ-btn" style="left:104px;top:509px"><svg width="10" height="10"><path d="M7,1 L3,5 L7,9" stroke="#fff" stroke-width="2" fill="none"/></svg></div>
<div class="abs thumb" style="left:143px;background:linear-gradient(135deg,#c9a27a,#6b4a3a)" role="img" aria-label="Listener with headphones"></div>
<div class="abs thumb" style="left:274px;background:radial-gradient(circle at 50% 40%,#6aa0c0,#1a2a3a 70%)" role="img" aria-label="Crowd at a light show"></div>
<div class="abs thumb" style="left:404px;background:linear-gradient(180deg,#2a2f45,#e0502a 60%,#222)" role="img" aria-label="DJ performing on stage"></div>
<div class="abs circ-btn" style="left:535px;top:509px"><svg width="10" height="10"><path d="M3,1 L7,5 L3,9" stroke="#fff" stroke-width="2" fill="none"/></svg></div>

<h2 class="abs sec-title" style="left:645px;top:450px">AWARDS/ACHIEVEMENTS:</h2>
<ul class="abs awards">
  <li>2010-All Confrence Freshman Team(Tranridge)</li>
  <li>2013-NRSCA Mid-East Region 1st Team</li>
  <li>2013-All Mid-East Region 1st Team</li>
  <li>2013-K-LAC Athlete of the Week (2X)</li>
  <li>2013-Ranked K-LAC Top 5-Steels (#1)</li>
</ul>
<div class="abs more">More Details »</div>
<div class="abs dot" style="left:578px"></div>
<div class="abs dot" style="left:601px"></div>

<h2 class="abs blog-title">LASTEST <b>BLOG</b></h2>
<div class="abs rule"></div>

<article>
  <div class="abs post-img" style="left:100px;top:709px;background:linear-gradient(135deg,#a01828,#3a1020 60%,#c04030)" role="img" aria-label="Group of friends at a party"></div>
  <p class="abs post-text" style="top:707px">Lorem ipsum dolor sit amet, consectetur adipiscing elit. Ut a metus diam, sit amet tristique risus. Aliquam dictum, lectus vel consequat malesuada, enim metus blandit urna, Lorem ipsum dolor sit amet, consectetur adipiscing elit. Ut a metus diam, sit amet tristique risus. Aliquam dictum, lectus vel consequat malesuada, enim metus blandit urna, vel sodales tellus nibh eget tortor.</p>
  <div class="abs meta" style="top:818px"><span><i></i>admin</span><span><i></i>April 24th, 2013</span><span><i></i>8 Comments</span></div>
</article>
<article>
  <div class="abs post-img" style="left:100px;top:877px;background:linear-gradient(135deg,#2a6a90,#3ab08a 50%,#1a3a2a)" role="img" aria-label="Friends celebrating at a club"></div>
  <p class="abs post-text" style="top:875px">Lorem ipsum dolor sit amet, consectetur adipiscing elit. Ut a metus diam, sit amet tristique risus. Aliquam dictum, lectus vel consequat malesuada, enim metus blandit urna, Lorem ipsum dolor sit amet, consectetur adipiscing elit. Ut a metus diam, sit amet tristique risus. Aliquam dictum, lectus vel consequat malesuada, enim metus blandit urna, vel sodales tellus nibh eget tortor.</p>
  <div class="abs meta" style="top:986px"><span><i></i>admin</span><span><i></i>April 24th, 2013</span><span><i></i>8 Comments</span></div>
</article>

<form class="abs form">
  <h2 class="form-title">Contact Us</h2>
  <div class="row" style="top:40px"><label>First Name<em>*</em></label><span></span></div>
  <div class="row" style="top:67px"><label>Last Name<em>*</em></label><span></span></div>
  <div class="row" style="top:94px"><label>Age</label><span></span></div>
  <div class="row" style="top:121px"><label>Zip Code</label><span></span></div>
  <div class="row" style="top:148px"><label>Email Address<em>*</em></label><span></span></div>
  <div class="row" style="top:175px"><label>Daytime Phone</label><span></span></div>
  <div class="row" style="top:202px"><label>Evening Phone</label><span></span></div>
  <div class="row" style="top:229px"><label>Comments</label><span style="height:36px"></span></div>
  <div class="submit">SUBMIT</div>
  <p class="form-note">After submitting, you will have the opportunity to upload demos of your music (optional) and provide other pertinent information about yourself, band, or group.</p>
</form>

<div class="abs footer-band"></div>
<section class="abs partners" aria-label="Partners">
  <svg style="position:absolute;left:14px;top:30px" width="18" height="24"><path d="M13,2 L4,12 L13,22" stroke="#222" stroke-width="3" fill="none"/></svg>
  <div class="badge" style="left:55px"></div>
  <div class="badge" style="left:166px"></div>
  <div class="badge" style="left:277px"></div>
  <div class="badge" style="left:388px"></div>
  <div class="badge" style="left:499px;width:90px"></div>
  <div class="badge" style="left:600px;width:100px"></div>
  <svg style="position:absolute;left:782px;top:30px" width="18" height="24"><path d="M5,2 L14,12 L5,22" stroke="#222" stroke-width="3" fill="none"/></svg>
</section>

<footer>
  <div class="abs foot-brand">
    <div class="brand-mark"></div>
    <div><div class="brand-name">Halvern</div><div class="brand-sub">The Halvern Sound Guild</div></div>
  </div>
  <div class="abs foot-links"><a>Home</a><span class="sep">|</span><a>Clients</a><span class="sep">|</span><a>Video music</a><span class="sep">|</span><a>High School Services</a><span class="sep">|</span><a>More...</a></div>
  <div class="abs copy">Copyright (C) halvernsoundguild.com. 2013.&nbsp; All Rights Reserved</div>
  <div class="abs foot-social"><span></span><span></span><span></span><span></span></div>
</footer>

</body>
</html>
```